Pull Up Banner - Recruitment Company

We would like a design for a pull up banner.

For context: we are a recruitment business. We specialise in helping people in healthcare industry to find jobs in Australia.

I have come up with several ideas and text for the banner. Feel free to use the following as you see appropriate:

- Our logo (see attached)
- 'Healthcare Recruitment Agency'
- Some sort of imagine / cartoon of medical professionals (ie. doctor, nurse, physiotherapist, speech pathologist). A cartoon is more friendly than committing to a photo
- 'Empowering your next career move'
- 'Discover tailored opportunities based on your career preferences'
- Dot points (allied health, nursing, medical imaging)
- Contact info at the bottom including our website (www.quellstaffing.com.au, our Social handle @quellstaffing, Mobile: XXXX XXX XXX. The title section for contact information could be 'Get in touch:'

Feel free to submit a couple of designs and we can merge aspects that look good on your designs and find the perfect fit.
Thank you
Updates

Hello,

Thank you for your initial submissions to this project. I appreciate the time you've invested.

After reviewing the first attempt, I'd like to share some feedback and initial observations:

- Professionalism and engagement: Is the overall appearance of the banner professional? It's crucial that we have a high-quality design as this will represent our business.

- Image selection: The image (whether cartoon or real people) appears quite generic. Please consider submitting the banner with a few different photos in the middle for us to choose from. Ensure the image is a good fit and not simply a generic stock photo.

- Contact section: Kindly remove the phone number; we no longer wish to include it on the banner. Instead, please include our website (www.quellstaffing.com.au) and Social handle (@quellstaffing).

- Color scheme: White, black, and red/pink are preferred, or alternatively, blue. However, please avoid incorporating too many different colors as it may detract from the professional appearance.

We will be printing the design on a banner and require it to look professional and engaging.

Thank you once again for your submissions. I hope the feedback provided above is helpful.

Warm regards,

Target Market(s)

Allied Health Australia

Font styles to use
Serif

Colors
0054AA
0677BA
7BADD7
CADEEF
E8F1F8
0094D4
00A9DD
6FCCEA
C7EBF8
E9F6FB
EB3D1F
EC4F4E
F09395
F8D3D4
FCEDEE

```html
<!DOCTYPE html>
<html lang="en">
<head>
<meta charset="utf-8">
<title>Quell Staffing – Pull Up Banner</title>
<link href="https://fonts.googleapis.com/css2?family=Tinos:wght@400;700&display=swap" rel="stylesheet">
<style>
  :root {
    --page: #ecebe8;
    --paper: #fbfbfa;
    --ink: #111111;
    --red: #e2403f;
    --peach: #f7d9ad;
    --orange: #ec8a4f;
    --sky: #6fccea;
  }
  html, body {
    margin: 0;
    width: 1200px;
    height: 1200px;
    overflow: hidden;
    background: var(--page);
    font-family: "Tinos", "Times New Roman", serif;
    color: var(--ink);
  }
  .banner {
    position: absolute;
    left: 385px;
    top: 38px;
    width: 430px;
    height: 1125px;
    background: var(--paper);
    box-shadow: 0 2px 10px rgba(0,0,0,0.12);
    overflow: hidden;
  }
  .banner-art {
    position: absolute;
    inset: 0;
  }
  .brand {
    position: absolute;
    top: 58px;
    left: 0;
    width: 100%;
    text-align: center;
  }
  .brand-name {
    font-weight: 700;
    font-size: 50px;
    letter-spacing: 6px;
    line-height: 1;
  }
  .brand-tag {
    margin-top: 18px;
    font-size: 11.5px;
    letter-spacing: 2.2px;
    text-transform: uppercase;
  }
  .headline {
    position: absolute;
    top: 168px;
    left: 0;
    width: 100%;
    margin: 0;
    text-align: center;
    font-weight: 700;
    font-size: 33px;
    line-height: 1.2;
    letter-spacing: -1px;
    text-transform: uppercase;
  }
  .subline {
    position: absolute;
    top: 256px;
    left: 40px;
    width: 350px;
    margin: 0;
    text-align: center;
    font-size: 21px;
    line-height: 1;
  }
  .sector {
    position: absolute;
    top: 848px;
    width: 120px;
    text-align: center;
    font-size: 22px;
    line-height: 1.05;
  }
  .sector--allied { left: 31px; }
  .sector--nursing { left: 160px; }
  .sector--imaging { left: 284px; }
  .contact-title {
    position: absolute;
    top: 914px;
    left: 101px;
    width: 234px;
    height: 52px;
    border-radius: 7px;
    background: var(--ink);
    color: var(--paper);
    font-weight: 700;
    font-size: 21px;
    letter-spacing: -0.5px;
    line-height: 52px;
    text-align: center;
    text-transform: uppercase;
  }
  .contact-list {
    position: absolute;
    top: 986px;
    left: 0;
    width: 100%;
    text-align: center;
    font-size: 20px;
    line-height: 30px;
  }
</style>
</head>
<body>
  <main class="banner">
    <svg class="banner-art" width="430" height="1125" viewBox="0 0 430 1125" aria-hidden="false">
      <defs>
        <radialGradient id="heroGlow" cx="0.5" cy="0.45" r="0.65">
          <stop offset="0" stop-color="#fbeccf"/>
          <stop offset="0.45" stop-color="var(--peach)"/>
          <stop offset="0.85" stop-color="var(--orange)"/>
          <stop offset="1" stop-color="#e7653c"/>
        </radialGradient>
        <linearGradient id="heroShade" x1="0" y1="0" x2="0" y2="1">
          <stop offset="0.55" stop-color="#7badd7" stop-opacity="0"/>
          <stop offset="1" stop-color="#7badd7" stop-opacity="0.55"/>
        </linearGradient>
      </defs>

      <!-- brand underline bar -->
      <rect class="brand-rule" x="95" y="128" width="240" height="0" fill="none"/>

      <!-- hero illustration area -->
      <g role="img" aria-label="Illustration of three smiling healthcare professionals in scrubs and white coats with stethoscopes, set against a warm orange flame-like backdrop">
        <path class="hero" d="M0 323 Q215 448 430 313 L430 800 Q215 700 0 850 Z" fill="url(#heroGlow)"/>
        <path class="hero-shade" d="M0 323 Q215 448 430 313 L430 800 Q215 700 0 850 Z" fill="url(#heroShade)"/>
      </g>

      <!-- top swoosh -->
      <path class="swoosh-line" d="M0 312 Q215 430 430 302" fill="none" stroke="var(--ink)" stroke-width="0.8"/>
      <path class="swoosh-band" d="M0 323 Q215 448 430 313" fill="none" stroke="var(--red)" stroke-width="7"/>

      <!-- lower swoosh -->
      <path class="swoosh-band" d="M0 850 Q215 700 430 800" fill="none" stroke="var(--red)" stroke-width="6"/>
      <path class="sector-base" d="M0 856 Q215 708 430 808 L430 1125 L0 1125 Z" fill="var(--paper)"/>

      <!-- sector badges -->
      <g class="badge" transform="translate(91 800)">
        <circle r="36" fill="var(--paper)" stroke="var(--ink)" stroke-width="7"/>
        <path d="M-36 0 A36 36 0 0 1 36 0" fill="none" stroke="var(--red)" stroke-width="7"/>
        <circle r="14" fill="none" stroke="var(--ink)" stroke-width="1.6" stroke-dasharray="5 3"/>
        <path d="M-3 -9 H3 V-3 H9 V3 H3 V9 H-3 V3 H-9 V-3 H-3 Z" fill="none" stroke="var(--ink)" stroke-width="1.6"/>
      </g>
      <g class="badge" transform="translate(220 778)">
        <circle r="36" fill="var(--paper)" stroke="var(--ink)" stroke-width="7"/>
        <path d="M-36 0 A36 36 0 0 1 36 0" fill="none" stroke="var(--red)" stroke-width="7"/>
        <g fill="none" stroke="var(--ink)" stroke-width="1.6">
          <circle cx="-11" cy="-5" r="5"/><path d="M-19 10 Q-11 -1 -3 10"/>
          <circle cx="0" cy="-7" r="5"/><path d="M-8 8 Q0 -3 8 8"/>
          <circle cx="11" cy="-5" r="5"/><path d="M3 10 Q11 -1 19 10"/>
        </g>
      </g>
      <g class="badge" transform="translate(344 795)">
        <circle r="36" fill="var(--paper)" stroke="var(--ink)" stroke-width="7"/>
        <path d="M-36 0 A36 36 0 0 1 36 0" fill="none" stroke="var(--red)" stroke-width="7"/>
        <g fill="none" stroke="var(--ink)" stroke-width="1.6">
          <rect x="-11" y="-15" width="22" height="29" rx="2"/>
          <rect x="-5" y="-18" width="10" height="5" rx="1"/>
          <path d="M-5 7 L5 -5"/>
          <path d="M3 6 H8 M3 9 H8"/>
        </g>
      </g>

      <!-- dividers -->
      <path class="divider" d="M153 850 V892 M287 850 V892" stroke="var(--red)" stroke-width="1.3" stroke-dasharray="4 3"/>
    </svg>

    <header class="brand">
      <div class="brand-name">QUELL</div>
      <div class="brand-tag">Staffing · Healthcare Recruitment Agency</div>
    </header>

    <h1 class="headline">Empowering your<br>next career move</h1>
    <p class="subline">Discover tailored opportunities based on your career preferences</p>

    <div class="sector sector--allied">Allied<br>Health</div>
    <div class="sector sector--nursing">Nursing</div>
    <div class="sector sector--imaging">Medical<br>Imaging</div>

    <div class="contact-title">Get in touch:</div>
    <div class="contact-list">
      <div class="contact-social">Social / @quellstaffing</div>
      <div class="contact-web">www.quellstaffing.com.au</div>
    </div>
  </main>
</body>
</html>
```